Jewelry Business card for general purpose. Elegant and simple

We are a jewelry group with 6 stores in Mexico and 30 years in business.

We need a BC that at leats includes the name, mail, phone number and physical location (street, municipality, and county; example "Paseo Olmeda 2140", "Avenida Sotillo", "Monterrey").
Optional: we are trying to reposition the brand with the association of life-events or moments and family. Such as: birth, marriage, graduation, birthdays. Christmast, mothers day and fathers day.

We are looking for something elegant but simple

Jewelry name: "Lunetti". Email: "lunettibrillo@correo-ejemplo.mx". Phone num "4172-3095".

Target Market(s)

General business card: from suppliers to clients. One segment outstand: couples gettineg married

Industry/Entity Type

Jewelry Store

Contact Information for Business Card

Loking for something simple but elegant.

Font styles to use
Decorative
Script

Requirements
Must have
• Must have name, address, and mail.
Nice to have
• It could have jewelry pictures/design. Maybe quotes. Or general words as background . currently we have a very simple card with one ring would like to see something different.
Should not have
• Include real people.

```html
<!DOCTYPE html>
<html lang="es">
<head>
<meta charset="utf-8">
<title>Lunetti — Tarjeta de presentación</title>
<link rel="stylesheet" href="https://fonts.googleapis.com/css2?family=Open+Sans:wght@400;600&display=swap">
<style>
  :root {
    --stage: #4a423d;
    --card: #0d0d0d;
    --card-edge: #1c1c1c;
    --gold: #f2a81d;
    --gold-deep: #d98c12;
    --silver: #d6d6d6;
    --ink: #f2f2f2;
    --divider: #262626;
  }
  * { box-sizing: border-box; margin: 0; padding: 0; }
  html, body {
    width: 1200px;
    height: 900px;
    overflow: hidden;
    background: var(--stage);
    font-family: "Open Sans", Arial, sans-serif;
  }
  .stage {
    width: 1200px;
    height: 900px;
    display: flex;
    align-items: center;
    justify-content: center;
    gap: 60px;
  }
  .card {
    width: 510px;
    height: 300px;
    background: var(--card);
    border: 1px solid var(--card-edge);
    box-shadow: 0 14px 30px rgba(0,0,0,.45);
    position: relative;
  }
  /* front */
  .card-front { display: flex; }
  .brand-panel {
    width: 230px;
    display: flex;
    align-items: center;
    justify-content: center;
    gap: 10px;
    border-right: 1px solid var(--divider);
    margin: 40px 0;
  }
  .brand-dot {
    width: 12px;
    height: 12px;
    border-radius: 50%;
    background: var(--gold);
  }
  .brand-name-front {
    font-weight: 600;
    font-size: 30px;
    color: var(--gold);
    letter-spacing: .5px;
  }
  .contact-panel {
    flex: 1;
    padding: 52px 20px 0 26px;
    color: var(--ink);
  }
  .person-name {
    font-weight: 600;
    font-size: 17px;
    color: var(--gold);
    line-height: 1.1;
  }
  .person-role { font-size: 12.5px; margin-bottom: 18px; }
  .address { font-size: 12.5px; line-height: 1.5; margin-bottom: 14px; }
  .contact-line {
    display: flex;
    align-items: center;
    gap: 9px;
    font-size: 12.5px;
    line-height: 1.6;
    white-space: nowrap;
  }
  .contact-line svg { flex: none; }
  /* back */
  .card-back {
    display: flex;
    align-items: center;
    justify-content: center;
  }
  .brand-name-back {
    font-weight: 400;
    font-size: 58px;
    color: var(--silver);
    letter-spacing: 1px;
  }
</style>
</head>
<body>
  <main class="stage">
    <section class="card card-front" aria-label="Frente de la tarjeta">
      <div class="brand-panel">
        <span class="brand-dot"></span>
        <span class="brand-name-front">Lunetti</span>
      </div>
      <div class="contact-panel">
        <p class="person-name">Mateo Ibarra</p>
        <p class="person-role">Managing Director</p>
        <p class="address">Paseo Olmeda 2140<br>Avenida Sotillo, Monterrey</p>
        <p class="contact-line">
          <svg width="10" height="10" viewBox="0 0 24 24" aria-hidden="true"><path fill="var(--gold)" d="M6.6 10.8a15.1 15.1 0 0 0 6.6 6.6l2.2-2.2c.3-.3.7-.4 1-.2 1.1.4 2.3.6 3.6.6.6 0 1 .4 1 1V20c0 .6-.4 1-1 1A17 17 0 0 1 3 4c0-.6.4-1 1-1h3.5c.6 0 1 .4 1 1 0 1.3.2 2.5.6 3.6.1.3 0 .7-.2 1z"/></svg>
          4172-3095
        </p>
        <p class="contact-line">
          <svg width="11" height="9" viewBox="0 0 22 16" aria-hidden="true"><rect width="22" height="16" rx="1.5" fill="var(--gold)"/><path d="M1 1l10 8 10-8" fill="none" stroke="var(--card)" stroke-width="1.6"/></svg>
          lunettibrillo@correo-ejemplo.mx
        </p>
      </div>
    </section>

    <section class="card card-back" aria-label="Reverso de la tarjeta">
      <span class="brand-name-back">Lunetti</span>
    </section>
  </main>
</body>
</html>
```